Business Card Design for company

We want new business cards. We'd like something different-- yet still highly professional. Our tagline is Providing leadership, delivering success. Stock photos are ok, as long as they are relevant and look upscale.

Target Market(s)

Architecture/Business Management Consulting/Engineering Consulting

Contact Information for Business Card

dark gray background with pops of blue might be good, but you tell me. You're the designers. Rounded corners might be nice, but again, you tell me.

Font styles to use
Serif
Sans Serif

Colors
3276b5
5c5c5c
9d9d9d
fbfbfb

Requirements
Nice to have
• Something different, but still very professional.

```html
<!DOCTYPE html>
<html lang="en">
<head>
<meta charset="utf-8">
<title>Corvane Partners – Business Cards</title>
<link href="https://fonts.googleapis.com/css2?family=Work+Sans:wght@300;400;600&display=swap" rel="stylesheet">
<style>
  :root {
    --brand-blue: #3276b5;
    --band-blue: #3a6fd0;
    --mid-gray: #5c5c5c;
    --light-gray: #9d9d9d;
    --paper-white: #fbfbfb;
    --card-black: #141517;
    --card-black-2: #1c1d20;
    --stage: #2c55a8;
  }
  * { margin: 0; padding: 0; box-sizing: border-box; }
  html, body { width: 1200px; height: 890px; overflow: hidden; }
  body {
    background: var(--stage);
    font-family: "Work Sans", Arial, sans-serif;
    color: var(--paper-white);
    position: relative;
  }
  .card {
    position: absolute;
    left: 250px;
    width: 700px;
    height: 400px;
    border-radius: 22px;
    overflow: hidden;
    background: linear-gradient(160deg, var(--card-black-2), var(--card-black));
    box-shadow: 0 10px 30px rgba(0,0,0,.35);
  }
  .card--back { top: 30px; }
  .card--front { top: 460px; }

  /* back */
  .back-brand {
    position: absolute; inset: 0;
    display: flex; flex-direction: column; align-items: center; justify-content: center;
  }
  .brand-name {
    font-weight: 400;
    color: var(--paper-white);
    letter-spacing: 0.08em;
    text-transform: uppercase;
  }
  .back-brand .brand-name { font-size: 46px; line-height: 1.1; text-align: center; }
  .tagline {
    margin-top: 22px;
    font-size: 13px;
    letter-spacing: 0.18em;
    text-transform: uppercase;
    color: var(--paper-white);
  }

  /* front */
  .front-brand {
    position: absolute; left: 60px; top: 95px; width: 250px;
    text-align: center;
  }
  .front-brand .brand-name { font-size: 30px; line-height: 1.2; }
  .divider {
    position: absolute; left: 335px; top: 70px;
    width: 1px; height: 200px; background: var(--brand-blue);
  }
  .contact { position: absolute; left: 365px; top: 82px; }
  .contact-name {
    font-size: 26px; font-weight: 600; letter-spacing: 0.06em;
    text-transform: uppercase; color: var(--band-blue);
  }
  .contact-title { font-size: 17px; margin: 4px 0 18px; color: var(--paper-white); }
  .contact-list { list-style: none; font-size: 14px; line-height: 1.75; }
  .contact-list li { display: flex; align-items: center; gap: 10px; }
  .contact-list svg { width: 12px; height: 12px; flex: none; }
  .accent-line {
    position: absolute; left: 0; right: 0; bottom: 72px;
    height: 2px; background: var(--band-blue);
  }
  .address-band {
    position: absolute; left: 0; right: 0; bottom: 0; height: 62px;
    background: var(--band-blue);
    display: flex; align-items: center; padding-left: 60px;
    font-size: 17px; color: var(--paper-white);
  }
</style>
</head>
<body>

<section class="card card--back">
  <div class="back-brand">
    <div class="brand-name">Corvane Partners</div>
    <div class="tagline">Guiding strategy | Building lasting results</div>
  </div>
</section>

<section class="card card--front">
  <div class="front-brand">
    <div class="brand-name">Corvane Partners</div>
  </div>
  <div class="divider"></div>
  <div class="contact">
    <div class="contact-name">Daniel Hoyt</div>
    <div class="contact-title">Design Consultant</div>
    <ul class="contact-list">
      <li>
        <svg viewBox="0 0 12 12" aria-hidden="true"><path d="M3 1 L5 3.5 L4 5 Q5 7 7 8 L8.5 7 L11 9 L9.5 11 Q5 11 2.5 7.5 Q1 5 1 2.5 Z" fill="var(--band-blue)"/></svg>
        +1 555-010-2840
      </li>
      <li>
        <svg viewBox="0 0 12 12" aria-hidden="true"><rect x="1" y="2.5" width="10" height="7" fill="none" stroke="var(--band-blue)" stroke-width="1.2"/><path d="M1 2.5 L6 6.5 L11 2.5" fill="none" stroke="var(--band-blue)" stroke-width="1.2"/></svg>
        OUTREACH@CORVANEPTN.COM
      </li>
      <li>
        <svg viewBox="0 0 12 12" aria-hidden="true"><rect x="1" y="2.5" width="10" height="7" fill="none" stroke="var(--band-blue)" stroke-width="1.2"/><path d="M1 2.5 L6 6.5 L11 2.5" fill="none" stroke="var(--band-blue)" stroke-width="1.2"/></svg>
        HELLO@CORVANEPTN.COM
      </li>
      <li>
        <svg viewBox="0 0 12 12" aria-hidden="true"><circle cx="6" cy="6" r="5" fill="none" stroke="var(--band-blue)" stroke-width="1.2"/><ellipse cx="6" cy="6" rx="2.2" ry="5" fill="none" stroke="var(--band-blue)" stroke-width="1"/><path d="M1 6 H11" stroke="var(--band-blue)" stroke-width="1"/></svg>
        www.corvaneptn.com
      </li>
    </ul>
  </div>
  <div class="accent-line"></div>
  <div class="address-band">1480 Harbor Crest Ave Tampa, Florida</div>
</section>

</body>
</html>
```